Design business cards and letterhead for real estate company

I need some graphic design. I would like someone to design business cards and letterhead for a real estate company. The logo is attached.

Two sided full color business cards.

The business cards needs the following on it:

Name: Peter Hollis
Position: Broker
Cell: 412-590-6637
Office: 415-203-9916 Ext: 101
Fax: 419-562-0174
Email: peterhollis@[login to view URL]
Website: [login to view URL]
Address: 457 Birchwood Lane
Utica, NY 13501

Pictures that need to be on it:
Logo
Agents Picture
Homevest Logo
MLS Logo
Multimillion dollar producer logo: this logo will not be on all business cards so the card needs to look nice with it and without it

Letterhead needs to have:
Logo
Address
Office phone: 413-826-4105
Fax: 417-945-2208
Email: contact@[login to view URL]

```html
<!DOCTYPE html>
<html lang="en">
<head>
<meta charset="utf-8">
<title>Kestrel Realty Stationery</title>
<link href="https://fonts.googleapis.com/css2?family=Montserrat:wght@400;500;600;700;800&display=swap" rel="stylesheet">
<style>
  :root {
    --red: #e31b23;
    --ink: #231f20;
    --dark: #2b2b2d;
    --paper: #ffffff;
    --ground: #e9e9ea;
    --muted: #6d6e71;
  }
  * { box-sizing: border-box; margin: 0; padding: 0; }
  html, body { width: 1200px; height: 800px; overflow: hidden; }
  body {
    background: var(--ground);
    font-family: "Montserrat", sans-serif;
    color: var(--ink);
    position: relative;
  }

  /* Letterhead */
  .letterhead {
    position: absolute; left: 90px; top: 50px;
    width: 495px; height: 700px;
    background: var(--paper);
    box-shadow: 0 2px 10px rgba(0,0,0,.08);
    overflow: hidden;
  }
  .letterhead .brand {
    position: absolute; top: 42px; left: 0; width: 100%;
    display: flex; justify-content: center; align-items: center; gap: 8px;
  }
  .brand-mark { width: 12px; height: 12px; background: var(--red); }
  .brand-name { font-weight: 800; text-transform: uppercase; letter-spacing: .5px; line-height: 1; }
  .letterhead .brand-name { font-size: 22px; color: var(--ink); }
  .letterhead .rule {
    position: absolute; top: 92px; left: 36px; right: 36px;
    height: 1px; background: var(--red);
  }
  .letterhead .footer-art { position: absolute; left: 0; bottom: 0; }
  .letterhead .contact-list {
    position: absolute; left: 26px; bottom: 22px;
    list-style: none; color: #fff;
  }
  .contact-list li { display: flex; align-items: center; gap: 12px; margin-top: 12px; font-size: 12px; font-weight: 500; line-height: 1.3; }
  .icon-dot {
    width: 24px; height: 24px; border-radius: 50%; background: #fff;
    display: flex; align-items: center; justify-content: center; flex: none;
  }
  .letterhead .website {
    position: absolute; right: 20px; bottom: 175px;
    display: flex; align-items: center; gap: 10px;
    color: #fff; font-weight: 700; font-size: 12px; line-height: 24px;
  }

  /* Business cards */
  .card {
    position: absolute; width: 480px; height: 272px;
    box-shadow: 0 2px 10px rgba(0,0,0,.1); overflow: hidden;
  }
  .card-front { left: 640px; top: 80px; background: var(--paper); }
  .card-back { left: 640px; top: 430px; background: var(--dark); }

  .card-front .brand { position: absolute; top: 24px; right: 26px; display: flex; align-items: center; gap: 7px; }
  .card-front .brand-name { font-size: 19px; color: var(--ink); }
  .card-front .divider { position: absolute; left: 0; top: 0; }
  .agent { position: absolute; left: 30px; top: 150px; }
  .agent-name { color: var(--red); font-weight: 700; font-size: 18px; }
  .agent-role { font-size: 11px; color: var(--muted); margin-top: 2px; }
  .agent-address { font-size: 11px; color: var(--ink); margin-top: 16px; line-height: 1.5; }
  .card-contacts {
    position: absolute; right: 30px; top: 86px; list-style: none;
    font-size: 10.5px; color: var(--ink);
  }
  .card-contacts li { display: flex; align-items: center; gap: 7px; margin-bottom: 7px; }
  .mini-dot { width: 14px; height: 14px; border-radius: 50%; background: var(--red); flex: none; }
  .card-front .badge { position: absolute; right: 30px; bottom: 30px; width: 24px; height: 24px; background: var(--ink); }
  .card-front .base { position: absolute; left: 0; bottom: 0; width: 100%; height: 8px; background: var(--dark); }

  .card-back .brand {
    position: absolute; top: 106px; left: 0; width: 100%;
    display: flex; justify-content: center; align-items: center; gap: 10px;
  }
  .card-back .brand-name { font-size: 32px; color: #fff; }
  .card-back .url {
    position: absolute; bottom: 40px; width: 100%; text-align: center;
    font-size: 11px; color: #bcbcbe; letter-spacing: .5px;
  }
</style>
</head>
<body>

<section class="letterhead">
  <div class="brand">
    <span class="brand-mark"></span>
    <span class="brand-name">Kestrel Realty</span>
  </div>
  <div class="rule"></div>

  <svg class="footer-art" width="495" height="230" viewBox="0 0 495 230" aria-hidden="true">
    <polygon points="262,20 495,20 495,66 274,66" fill="var(--red)"/>
    <polygon points="284,66 495,66 495,100 292,100" fill="var(--dark)"/>
    <polygon points="0,80 248,80 285,230 0,230" fill="var(--dark)"/>
    <polygon points="258,80 272,80 309,230 295,230" fill="var(--red)"/>
  </svg>

  <div class="website">
    <span class="icon-dot">
      <svg width="14" height="14" viewBox="0 0 14 14" aria-hidden="true"><circle cx="7" cy="7" r="5.5" fill="none" stroke="var(--red)" stroke-width="1.4"/><path d="M1.5 7h11M7 1.5c-2.4 3-2.4 8 0 11M7 1.5c2.4 3 2.4 8 0 11" fill="none" stroke="var(--red)" stroke-width="1"/></svg>
    </span>
    www.kestrelhomes.com
  </div>

  <ul class="contact-list">
    <li>
      <span class="icon-dot"><svg width="12" height="14" viewBox="0 0 12 14" aria-hidden="true"><path d="M6 1a4 4 0 0 0-4 4c0 3 4 8 4 8s4-5 4-8a4 4 0 0 0-4-4z" fill="var(--dark)"/><circle cx="6" cy="5" r="1.5" fill="#fff"/></svg></span>
      <span>457 Birchwood Lane<br>Dunmore, PA 18512</span>
    </li>
    <li>
      <span class="icon-dot"><svg width="12" height="12" viewBox="0 0 12 12" aria-hidden="true"><path d="M2.5 1l2 2.5-1.2 1.2a7 7 0 0 0 4 4l1.2-1.2L11 9.5 9.8 11C5 11 1 7 1 2.2z" fill="var(--dark)"/></svg></span>
      <span>413-826-4105<br>417-945-2208 Ext : 204</span>
    </li>
    <li>
      <span class="icon-dot"><svg width="12" height="10" viewBox="0 0 12 10" aria-hidden="true"><rect x=".5" y=".5" width="11" height="9" fill="none" stroke="var(--dark)"/><path d="M.5 .5 6 5.5 11.5 .5" fill="none" stroke="var(--dark)"/></svg></span>
      <span>peterhollis@kestrelhomes.com</span>
    </li>
  </ul>
</section>

<section class="card card-front">
  <svg class="divider" width="480" height="272" viewBox="0 0 480 272" aria-hidden="true">
    <line x1="0" y1="140" x2="300" y2="60" stroke="var(--red)" stroke-width="1"/>
  </svg>
  <div class="brand">
    <span class="brand-mark"></span>
    <span class="brand-name">Kestrel Realty</span>
  </div>
  <div class="agent">
    <div class="agent-name">Peter Hollis</div>
    <div class="agent-role">Broker</div>
    <div class="agent-address">457 Birchwood Lane<br>Dunmore, PA 18512</div>
  </div>
  <ul class="card-contacts">
    <li><span class="mini-dot"></span>Cell: 412-590-6637</li>
    <li><span class="mini-dot"></span>Office: 415-203-9916 Ext: 204</li>
    <li><span class="mini-dot"></span>Fax: 419-562-0174</li>
    <li><span class="mini-dot"></span>peterhollis@kestrelhomes.com</li>
  </ul>
  <div class="badge"></div>
  <div class="base"></div>
</section>

<section class="card card-back">
  <div class="brand">
    <span class="brand-mark"></span>
    <span class="brand-name">Kestrel Realty</span>
  </div>
  <div class="url">www.kestrelhomes.com</div>
</section>

</body>
</html>
```